Email Marketing for HR and Career Consulting Company

I am looking for a email marketing template that will be developed in HTML format. Right now, we need PSD file format.

The content will include:

1. Featured / Poplar Blog post
2. Latest blog post this week
3. Latest jobs this week
4. Connect with us (social media)

This is a bi-weekly template which we will be sending to people who sign up our weekly newsletter. The purpose of the newsletter is to provide career advise and also latest jobs that's available from our company so that we can redirect them to our career page or apply to our latest jobs.
Updates

Project Deadline Extended
Reason: I am extending this deadline as I would like to see more designs. So far, I have only shortlisted one design that is close to what I am looking for. To all designers, please note that your design would have to be practical and easy to navigate. It also must take into consideration that when we develop this into html, it will b responsive.

Target Market(s)

Job seekers - age group 25 - 45

Industry/Entity Type

Consulting

Font styles to use
Other font styles liked:
• Helvetical

Colors
0492cd
e34197
ec1f27
85cae6
33a6d7
85acd3
eda3c7
e667a6
f59195

Requirements
Must have
• 1. Social media icons
• 2. Links - jobs, contact us
• 3. Popular career advice
• 4. Latest career advice
• 5. Featured jobs
• 6. Popular jobs
Nice to have
• I would like to see clean and minimalist design. Please try to avoid black color. Use pastel colors as much as possible. Our website is www.careerpondly.com.sg
Should not have
• Should avoid black and dark colors

```html
<!DOCTYPE html>
<html lang="en">
<head>
<meta charset="utf-8">
<title>Careerpondly Newsletter</title>
<link href="https://fonts.googleapis.com/css2?family=Roboto:wght@300;400;500;700&display=swap" rel="stylesheet">
<style>
:root{
  --cyan:#3bb3dc;
  --cyan-deep:#2a9fcf;
  --pink:#f0656f;
  --pink-soft:#f59195;
  --slate:#85acd3;
  --blue-text:#2b8fd0;
  --ink:#55606b;
  --muted:#7c8790;
  --rule:#d9e3ea;
  --footer:#a9abad;
  --white:#ffffff;
}
*{margin:0;padding:0;box-sizing:border-box}
html,body{width:1200px;height:2916px;overflow:hidden;background:var(--white)}
body{font-family:"Roboto",Helvetica,Arial,sans-serif;color:var(--ink);position:relative}
.abs{position:absolute;left:0;width:1200px}
.notice-bar{top:0;height:48px;background:var(--pink-soft);color:var(--white);font-size:22px;font-weight:300;display:flex;align-items:center;justify-content:center}
.brand{top:48px;height:232px;display:flex;flex-direction:column;align-items:center;justify-content:center;gap:10px}
.brand-mark{width:84px;height:84px;border-radius:50%;background:var(--cyan-deep)}
.brand-name{font-size:38px;font-weight:500;color:var(--blue-text);line-height:1}
.brand-tag{font-size:13px;color:var(--muted);letter-spacing:1px}
.section-band{display:flex;align-items:center;justify-content:center;color:var(--white);font-size:52px;font-weight:400;letter-spacing:1px}
.advice{top:280px;height:580px;background:var(--cyan)}
.advice .section-band{height:110px}
.advice-visual{position:absolute;left:48px;top:100px;width:1104px;height:452px;background:linear-gradient(135deg,#cfe3ee 0%,#9fc4d8 55%,#6f9fb8 100%);border:6px solid var(--white)}
.advice-headline{position:absolute;left:140px;top:34px;width:812px;padding:22px 20px;background:rgba(59,179,220,.82);border:3px solid var(--white);color:var(--white);text-align:center;font-size:42px;font-weight:500;line-height:1.25}
.btn{display:flex;align-items:center;justify-content:center;color:var(--white);font-weight:500;border-radius:4px}
.advice-btn{position:absolute;left:392px;top:372px;width:320px;height:66px;background:var(--cyan);font-size:38px;letter-spacing:1px}
.jobs-band{top:864px;height:96px;background:var(--pink)}
.job-list{top:972px;left:48px;width:1104px}
.job-row{height:134px;border-bottom:2px solid var(--rule);display:flex;flex-direction:column;justify-content:center;gap:6px}
.job-title{font-size:40px;color:var(--blue-text);font-weight:400;line-height:1.2;white-space:nowrap}
.job-meta{display:flex;align-items:center;justify-content:space-between}
.job-tags{font-size:17px;color:var(--blue-text);letter-spacing:.5px;text-transform:uppercase}
.job-tags span+span::before{content:"|";margin:0 8px;color:var(--rule)}
.apply-btn{width:232px;height:50px;background:var(--pink);font-size:22px;letter-spacing:1px}
.blog-band{top:1380px;height:100px;background:var(--slate)}
.blog-card{position:absolute;top:1520px;width:532px}
.blog-card.left{left:48px}
.blog-card.right{left:620px}
.blog-visual{width:532px;height:320px}
.blog-visual.bye{background:linear-gradient(160deg,#bfe0e6,#8fc3cf)}
.blog-visual.plan{background:linear-gradient(160deg,#f7a2a6,#ee6d74)}
.blog-title{font-size:29px;font-weight:400;color:var(--ink);line-height:1.35;margin-top:22px;height:80px;white-space:nowrap}
.blog-text{font-size:20px;color:var(--muted);line-height:1.45;margin-top:18px;height:60px}
.read-btn{width:260px;height:56px;background:var(--slate);font-size:22px;font-weight:400;margin-top:18px}
.week-band{top:2160px;height:92px;background:var(--pink)}
.week-job{position:absolute;left:48px;top:2280px;width:560px}
.week-title{font-size:42px;color:#e0474f;line-height:1.2;font-weight:400}
.week-text{font-size:22px;color:var(--muted);line-height:1.45;margin-top:18px}
.week-btn{width:380px;height:64px;background:var(--pink);font-size:24px;letter-spacing:1px;margin:30px 0 0 40px}
.week-visual{position:absolute;left:628px;top:2272px;width:532px;height:330px;background:linear-gradient(150deg,#dfe5ea,#9fb0bf 60%,#6f8597)}
.social{top:2668px;height:100px;display:flex;justify-content:center;gap:44px;align-items:center}
.social-dot{width:84px;height:84px;border-radius:50%}
.footer{top:2800px;height:116px;background:var(--footer);color:var(--white);font-size:20px;font-weight:300;display:flex;flex-direction:column;align-items:center;justify-content:center;gap:14px}
</style>
</head>
<body>
  <div class="abs notice-bar">If this e-mail is not displayed properly, CLICK HERE.</div>

  <header class="abs brand">
    <div class="brand-mark"></div>
    <div class="brand-name">careerpondly</div>
    <div class="brand-tag">career consulting</div>
  </header>

  <section class="abs advice">
    <h2 class="section-band">LATEST CAREER ADVICE</h2>
    <div class="advice-visual" role="img" aria-label="Photo of a hand pointing at a job search note with a pen and a clipboard">
      <div class="advice-headline">Contract Jobs:<br>Can They Really Be A Career Option?</div>
      <div class="btn advice-btn">READ MORE</div>
    </div>
  </section>

  <h2 class="abs section-band jobs-band">LATEST JOBS THIS WEEK</h2>
  <div class="abs job-list">
    <div class="job-row">
      <div class="job-title">Senior / Recruitment Consultant - Executive Search Division</div>
      <div class="job-meta">
        <div class="job-tags"><span>Singapore</span><span>Human Resource</span><span>Full-Time</span></div>
        <div class="btn apply-btn">APPLY NOW</div>
      </div>
    </div>
    <div class="job-row">
      <div class="job-title">TMS Support Analyst, APAC</div>
      <div class="job-meta">
        <div class="job-tags"><span>Singapore</span><span>Information Technology</span><span>Full-Time</span></div>
        <div class="btn apply-btn">APPLY NOW</div>
      </div>
    </div>
    <div class="job-row">
      <div class="job-title">Logistics Manager - Fashion Retail</div>
      <div class="job-meta">
        <div class="job-tags"><span>Singapore</span><span>Logistics</span><span>Full-Time</span></div>
        <div class="btn apply-btn">APPLY NOW</div>
      </div>
    </div>
  </div>

  <h2 class="abs section-band blog-band">MORE FROM OUR BLOG</h2>
  <article class="blog-card left">
    <div class="blog-visual bye" role="img" aria-label="Illustration of a man leaving work with a box, saying bye"></div>
    <h3 class="blog-title">10 Things to Expect After<br>You have Quit Your Job</h3>
    <p class="blog-text">Congratulations! You have just quit your job and you are taking a well-deserved break.</p>
    <div class="btn read-btn">Read more...</div>
  </article>
  <article class="blog-card right">
    <div class="blog-visual plan" role="img" aria-label="Illustration of a hand holding a stopwatch"></div>
    <h3 class="blog-title">Your Five-Year Plan<br>Ultimate and Easy Ways for Success</h3>
    <p class="blog-text">Whether in work or play, research suggests that the happiest individuals are those with ...</p>
    <div class="btn read-btn">Read more...</div>
  </article>

  <h2 class="abs section-band week-band">JOB OF THE WEEK</h2>
  <div class="week-job">
    <h3 class="week-title">Manager, Trade Compliance, Service Logistic, APAC</h3>
    <p class="week-text">The role purpose is to manage Network customer as a single point of contact for performance, relationship and escalation management, to generate new business leads to support growth...</p>
    <div class="btn week-btn">APPLY FOR THIS JOB</div>
  </div>
  <div class="week-visual" role="img" aria-label="Photo of business colleagues in a meeting"></div>

  <nav class="abs social" aria-label="Social media links">
    <div class="social-dot" style="background:#4f73b5" aria-label="Social link 1"></div>
    <div class="social-dot" style="background:#e0564a" aria-label="Social link 2"></div>
    <div class="social-dot" style="background:#a05aa8" aria-label="Social link 3"></div>
    <div class="social-dot" style="background:#2f82b8" aria-label="Social link 4"></div>
    <div class="social-dot" style="background:#d9414c" aria-label="Social link 5"></div>
    <div class="social-dot" style="background:#4fb3e6" aria-label="Social link 6"></div>
    <div class="social-dot" style="background:#3aa5d8" aria-label="Social link 7"></div>
    <div class="social-dot" style="background:#e5484d" aria-label="Social link 8"></div>
  </nav>

  <footer class="abs footer">
    <div>Sent by: Company Name, Address, Street Number 1</div>
    <div>View online | Unsubscribe</div>
  </footer>
</body>
</html>
```